Commercial Real Estate Executive Recruiting Firm Needs Business Card Design

We need a business card design for BRAMLEY | Executive Recruiting - an executive recruiting firm focused exclusively on the commercial real estate industry. We place professionals ranging from Analyst to the Executive Office covering all investment/finance disciplines (acquisitions, asset management, capital markets, etc.) in all product types (office, retail, multifamily, industrial, land, etc.). We have a passion for helping people (clients and candidates) and have a reputation for being open and honest in our recruiting - and yes, very successful. We have recently developed a new logo and would like to update our business cards as well. I've uploaded some information about our company that contains the new logo.

Target Market(s)

Commercial Real Estate professionals. Primarily in the US. These are typically, smart, driven professionals with finance degrees and MBAs. Primarily men between the ages of 25 and 55.

Industry/Entity Type

Real Estate

Font styles to use
Other font styles liked:
• The font for "BRAMLEY" is Blair ITC (Medium), and "executive recruiting" is Gotham (Book).

Requirements
Must have
• I like the idea of white background on one side and solid color (blue, black, etc.) on back of card.

Would like to utilize the fonts in the logo (to the extent possible) so as to not have too many fonts on card.
Nice to have
• I think the roles (i.e., Acquisitions, Asset Management, etc.,...) is probably likely best placed on the back side of the card with the logo maybe. See attached current business card for content.

```html
<!DOCTYPE html>
<html lang="en">
<head>
<meta charset="utf-8">
<title>BRAMLEY | Executive Recruiting – Business Cards</title>
<link href="https://fonts.googleapis.com/css2?family=PT+Sans:wght@400;700&display=swap" rel="stylesheet">
<style>
  :root {
    --canvas-bg: #efece6;
    --card-light: #eaf0f9;
    --card-mid: #b9cfeb;
    --card-deep: #3d87cf;
    --ink: #2b2b2b;
    --ink-soft: #4a4f57;
    --icon-blue: #3f86cc;
    --mark-blue: #2f6db0;
    --shadow: rgba(40, 40, 40, 0.28);
  }
  * { box-sizing: border-box; margin: 0; padding: 0; }
  html, body {
    width: 1200px; height: 900px; overflow: hidden;
    background: var(--canvas-bg);
    font-family: "PT Sans", "Trebuchet MS", sans-serif;
    color: var(--ink);
  }
  .canvas { position: relative; width: 1200px; height: 900px; }

  .card {
    position: absolute;
    width: 520px; height: 298px;
    background: linear-gradient(to top right, var(--card-light) 0%, var(--card-light) 25%, var(--card-mid) 62%, var(--card-deep) 100%);
    box-shadow: 6px 8px 18px var(--shadow);
  }
  .card--front { left: 50px; top: 170px; }
  .card--back  { left: 630px; top: 430px; }

  /* Front */
  .holder { position: absolute; left: 0; top: 18px; width: 100%; text-align: center; padding-right: 110px; }
  .holder__name { font-size: 24px; font-weight: 700; letter-spacing: 4px; color: var(--ink); line-height: 28px; }
  .holder__title { font-size: 11px; letter-spacing: 1.6px; color: var(--ink-soft); margin-top: 4px; }

  .contact-list { position: absolute; left: 150px; top: 84px; list-style: none; }
  .contact-list li {
    display: flex; align-items: flex-start; gap: 16px;
    font-size: 15px; letter-spacing: 1px; color: var(--ink-soft);
    line-height: 18px; margin-bottom: 5px;
  }
  .contact-list svg { width: 18px; height: 18px; flex: none; fill: var(--icon-blue); }

  .lockup { position: absolute; display: flex; align-items: center; }
  .lockup__square { width: 40px; height: 40px; background: var(--mark-blue); flex: none; }
  .lockup__rule { width: 2px; height: 46px; background: var(--ink-soft); margin: 0 14px; opacity: .6; }
  .lockup__name { color: var(--ink); font-weight: 400; line-height: 1; }
  .lockup__name .word { display: block; font-size: 34px; letter-spacing: 9px; }
  .lockup__name .tag { display: block; font-size: 15px; letter-spacing: 3.4px; margin-top: 3px; }

  .card--front .lockup { left: 56px; bottom: 18px; }

  /* Back */
  .card--back .brand { position: absolute; left: 0; top: 62px; width: 100%; text-align: center; }
  .card--back .brand .lockup__square { display: block; margin: 0 auto 14px; width: 44px; height: 44px; }
  .card--back .lockup__name .word { font-size: 40px; letter-spacing: 11px; }
  .card--back .lockup__name .tag { font-size: 16px; letter-spacing: 3.6px; }
  .web { margin-top: 16px; font-size: 17px; letter-spacing: 2.4px; color: var(--ink-soft); }
</style>
</head>
<body>
<main class="canvas">

  <section class="card card--front" aria-label="Business card front">
    <header class="holder">
      <h1 class="holder__name">JORDAN</h1>
      <p class="holder__title">DESIGNATION</p>
    </header>

    <ul class="contact-list">
      <li>
        <svg viewBox="0 0 24 24" aria-hidden="true"><path d="M2 5h20v14H2z"/><path d="M3 6.5l9 7 9-7" fill="none" stroke="#fff" stroke-width="1.4"/></svg>
        <span>jordan@bramleyrecruiting.com</span>
      </li>
      <li>
        <svg viewBox="0 0 24 24" aria-hidden="true"><path d="M6.6 10.8a15 15 0 006.6 6.6l2.2-2.2c.3-.3.7-.4 1-.2 1.1.4 2.3.6 3.6.6.6 0 1 .4 1 1V20c0 .6-.4 1-1 1A17 17 0 013 4c0-.6.4-1 1-1h3.5c.6 0 1 .4 1 1 0 1.3.2 2.5.6 3.6.1.3 0 .7-.2 1z"/></svg>
        <span>214-555-0147</span>
      </li>
      <li>
        <svg viewBox="0 0 24 24" aria-hidden="true"><path d="M12 3c-3.3 0-6 2.7-6 6v6c0 3.3 2.7 6 6 6s6-2.7 6-6V9c0-3.3-2.7-6-6-6zm-.8 2h1.6v5h-1.6z"/></svg>
        <span>bramleyrecruiting.com</span>
      </li>
      <li>
        <svg viewBox="0 0 24 24" aria-hidden="true"><path d="M12 2a7 7 0 00-7 7c0 5.2 7 13 7 13s7-7.8 7-13a7 7 0 00-7-7zm0 9.5A2.5 2.5 0 1112 6.5a2.5 2.5 0 010 5z"/></svg>
        <span>2750 Larkspur Lane<br>Plano, Texas 75024</span>
      </li>
    </ul>

    <div class="lockup">
      <span class="lockup__square" aria-hidden="true"></span>
      <span class="lockup__rule" aria-hidden="true"></span>
      <p class="lockup__name"><span class="word">BRAMLEY</span><span class="tag">executive recruiting</span></p>
    </div>
  </section>

  <section class="card card--back" aria-label="Business card back">
    <div class="brand">
      <span class="lockup__square" aria-hidden="true"></span>
      <p class="lockup__name"><span class="word">BRAMLEY</span><span class="tag">executive recruiting</span></p>
      <p class="web">www.bramleyrecruiting.com</p>
    </div>
  </section>

</main>
</body>
</html>
```